Cleaning Company Website Design

I am looking for a website design that has my contact information on each page (Call or Text and my e-mail). It should have the main landing page and than pages for Residential Cleaning (Move In/Move Out, Weekly, and Bi-Weekly Cleaning), Commercial Cleaning (Move In/Move Out, Weekly, and Bi-Weekly Cleaning), New Construction Cleaning (Residential, Commercial, and Industrial), and Apartment Turn cleaning for Property Managers. It should list that we carry insurance as well.

Target Market(s)

Residential and Commercial Customers

Industry/Entity Type

Cleaning

Coding

Coded - Design and coding required

Number of Pages Required

5+ page

Requirements
Must have
• A clean professional looking website

```html
<!DOCTYPE html>
<html lang="en">
<head>
<meta charset="utf-8">
<title>BrightNest Cleaning</title>
<link href="https://fonts.googleapis.com/css2?family=Fira+Sans:wght@300;400;500;600;700&family=Merriweather:wght@300;400&display=swap" rel="stylesheet">
<style>
:root{
  --blue:#2a86c8;
  --blue-deep:#1a5fa8;
  --teal:#3cb6ad;
  --teal-light:#dff3f2;
  --teal-soft:#c4ebe8;
  --ink:#1e2a33;
  --muted:#7b8790;
  --white:#ffffff;
  --yellow:#e9e29a;
  --sky:#8cc0e3;
  --star:#f08a5d;
}
*{margin:0;padding:0;box-sizing:border-box}
html,body{width:1200px;height:3636px;overflow:hidden}
body{position:relative;background:var(--white);font-family:"Merriweather",serif;color:var(--ink)}
.abs{position:absolute}
h1,h2,h3,h4,.sans{font-family:"Fira Sans",sans-serif}
.muted{color:var(--muted);font-size:11px;line-height:17px;font-weight:300}
.btn{position:absolute;display:flex;align-items:center;justify-content:center;background:linear-gradient(90deg,var(--blue),var(--teal));color:#fff;font-family:"Merriweather",serif;font-size:11px}
.arrow-btn{position:absolute;width:28px;height:28px;border-radius:50%;background:#fff;box-shadow:0 2px 6px rgba(0,0,0,.12);display:flex;align-items:center;justify-content:center}
.arrow-btn svg{width:12px;height:12px}
.photo{position:absolute}
/* header */
.logo{position:absolute;left:193px;top:30px;display:flex;align-items:center;gap:8px}
.logo-mark{width:18px;height:18px;background:var(--blue);border-radius:3px}
.logo-name{font-family:"Fira Sans",sans-serif;font-weight:600;font-size:17px;color:var(--blue);letter-spacing:.5px;line-height:20px}
.top-contact{position:absolute;top:32px;left:632px;display:flex;gap:26px;color:#fff;font-size:11px;align-items:center}
.top-contact span{display:flex;align-items:center;gap:10px}
/* hero */
.hero-title{position:absolute;left:193px;top:160px;font-weight:700;font-size:42px;letter-spacing:1px;color:var(--ink)}
.hero-sub{position:absolute;left:193px;top:216px;font-weight:300;font-size:38px;letter-spacing:1px;color:var(--ink)}
.hero-tag{position:absolute;left:193px;top:278px;font-size:19px;line-height:30px;width:400px}
/* about */
.section-title{font-family:"Fira Sans",sans-serif;font-weight:500;font-size:27px;line-height:32px;color:var(--ink)}
.feature{position:absolute;left:648px;width:360px}
.feature .tick{position:absolute;left:0;top:0;width:20px;height:20px;border-radius:50%;background:var(--teal-light);display:flex;align-items:center;justify-content:center}
.feature h4{margin-left:34px;font-weight:500;font-size:14px;margin-bottom:6px}
.feature p{margin-left:34px}
/* services */
.tab{position:absolute;top:1211px;height:37px;width:251px;transform:skewX(-14deg);border:1px solid #d8dee2;background:#fff}
.tab.active{background:var(--blue);border-color:var(--blue)}
.tab-label{position:absolute;top:1211px;height:37px;width:251px;display:flex;align-items:center;justify-content:center;gap:10px;font-family:"Fira Sans",sans-serif;font-size:14px;color:#555}
.tab-label.active{color:#fff}
.service-card{position:absolute;left:193px;top:1273px;width:812px;height:375px;background:#fff;box-shadow:0 4px 16px rgba(0,0,0,.05)}
/* team */
.member{position:absolute;top:1893px;width:187px;height:294px;border-radius:4px;overflow:hidden}
.member .shade{position:absolute;left:0;right:0;bottom:0;height:90px;background:linear-gradient(transparent,rgba(0,0,0,.7))}
.member .name{position:absolute;left:12px;bottom:26px;color:#fff;font-family:"Fira Sans",sans-serif;font-weight:500;font-size:11px}
.member .role{position:absolute;left:12px;bottom:12px;color:#e8e8e8;font-size:9px}
/* testimonials */
.review{position:absolute;top:2439px;width:237px;height:286px;background:#fff;text-align:center;padding-top:20px}
.review .avatar{width:44px;height:44px;border-radius:50%;margin:0 auto 8px}
.review h4{font-weight:500;font-size:12px;color:#444}
.review .role{font-size:9px;color:var(--muted);margin-top:4px}
.review .stars{margin:14px auto 10px;display:flex;justify-content:center;gap:9px}
.review p{font-size:10px;line-height:19px;color:#666;padding:0 18px;font-weight:300}
/* contact */
.contact-row{position:absolute;left:193px;display:flex;align-items:center;gap:22px;font-size:11px}
.field{position:absolute;left:633px;width:350px;border-bottom:1px solid #d9dee1;font-size:9px;color:#666;padding-bottom:8px}
/* footer */
.footer{position:absolute;left:0;top:3386px;width:1200px;height:250px;background:linear-gradient(135deg,var(--blue-deep) 0%,var(--blue) 45%,var(--teal) 100%);overflow:hidden;color:#fff}
.footer h4{font-weight:500;font-size:12px;margin-bottom:14px;text-decoration:underline;text-underline-offset:4px}
.footer li{list-style:none;font-size:9px;margin-bottom:12px;opacity:.9}
</style>
</head>
<body>

<!-- HERO -->
<svg class="abs" style="left:0;top:0" width="1200" height="560" viewBox="0 0 1200 560" aria-hidden="true">
  <path d="M0 0 H300 C360 40 330 120 260 180 C190 240 90 250 0 270 Z" fill="var(--teal-light)"/>
  <defs>
    <linearGradient id="heroPhoto" x1="0" y1="0" x2="1" y2="1">
      <stop offset="0" stop-color="#b9a89a"/>
      <stop offset=".45" stop-color="#8e8fa3"/>
      <stop offset="1" stop-color="#5a7fa8"/>
    </linearGradient>
  </defs>
  <path d="M520 120 C600 60 760 40 900 60 C1060 80 1160 160 1200 240 V560 C1130 560 1090 480 1020 450 C940 420 880 470 800 440 C720 410 650 450 590 430 Z" fill="var(--sky)" opacity=".5"/>
</svg>
<svg class="abs" style="left:0;top:0" width="1200" height="560" viewBox="0 0 1200 560" role="img" aria-label="Photo of two cleaners wiping a sofa and vacuuming a living room floor">
  <path d="M470 0 H1200 V550 C1150 540 1120 470 1060 440 C980 400 900 460 800 440 C700 420 640 440 580 420 C480 380 420 260 440 150 C450 90 460 40 470 0 Z" fill="url(#heroPhoto)"/>
  <path d="M600 420 C640 330 720 300 800 330 C880 360 980 280 1060 240 C1120 210 1170 220 1200 240 V550 C1150 540 1120 470 1060 440 C980 400 900 460 800 440 C700 420 640 440 600 420 Z" fill="var(--teal)" opacity=".35"/>
</svg>

<div class="logo"><div class="logo-mark"></div><div class="logo-name">BRIGHTNEST</div></div>

<div class="top-contact">
  <span><svg width="18" height="18" viewBox="0 0 24 24" fill="#fff"><path d="M6.6 10.8a15.1 15.1 0 0 0 6.6 6.6l2.2-2.2c.3-.3.7-.4 1-.2 1.1.4 2.3.6 3.6.6.6 0 1 .4 1 1V20c0 .6-.4 1-1 1A17 17 0 0 1 3 4c0-.6.4-1 1-1h3.5c.6 0 1 .4 1 1 0 1.3.2 2.5.6 3.6.1.3 0 .7-.2 1z"/></svg>(555) 014-3820</span>
  <span><svg width="20" height="16" viewBox="0 0 24 18" fill="none" stroke="#fff" stroke-width="2"><rect x="1" y="1" width="22" height="16" rx="2"/><path d="M1 2l11 8 11-8"/></svg>hello@brightnestclean.com</span>
  <span><svg width="14" height="12" viewBox="0 0 14 12" stroke="#fff" stroke-width="1.6"><path d="M0 1h14M4 6h10M0 11h14"/></svg></span>
</div>

<h1 class="hero-title">BRIGHTNEST</h1>
<div class="hero-sub sans">CLEANING</div>
<p class="hero-tag">Quality driven and reliable to take of all your cleaning needs!!!</p>
<div class="btn" style="left:193px;top:363px;width:126px;height:34px">Discover Services</div>

<div class="arrow-btn" style="left:939px;top:452px"><svg viewBox="0 0 12 12" fill="none" stroke="#555" stroke-width="1.5"><path d="M8 2L4 6l4 4"/></svg></div>
<div class="arrow-btn" style="left:976px;top:452px"><svg viewBox="0 0 12 12" fill="none" stroke="var(--blue)" stroke-width="1.5"><path d="M4 2l4 4-4 4"/></svg></div>

<!-- TEAL BAND (services) -->
<svg class="abs" style="left:0;top:840px" width="1200" height="870" viewBox="0 0 1200 870" aria-hidden="true">
  <path d="M0 20 C120 60 220 120 360 150 C560 190 820 130 1000 70 C1100 40 1160 50 1200 60 V870 H0 Z" fill="var(--teal-light)"/>
  <path d="M0 830 C40 790 110 790 170 800 C230 810 270 780 320 800 C360 815 340 870 300 870 H0 Z" fill="var(--teal)" opacity=".75"/>
  <path d="M360 870 C380 810 450 790 500 830 C520 850 520 870 520 870 Z" fill="var(--sky)"/>
  <path d="M550 870 C580 800 680 780 760 800 C800 810 830 840 840 870 Z" fill="#c6d8df"/>
  <path d="M970 870 C990 780 1080 730 1150 750 C1190 760 1180 820 1170 870 Z" fill="var(--yellow)"/>
</svg>

<!-- ABOUT -->
<div class="photo" style="left:193px;top:553px;width:360px;height:452px;background:linear-gradient(160deg,#c9c1b6,#7c7a80 60%,#3f4a63);border-radius:4px" role="img" aria-label="Photo of two cleaners dusting a TV stand and vacuuming a carpet"></div>
<div class="abs" style="left:110px;top:596px;width:165px;height:210px;background:#fff;box-shadow:0 4px 14px rgba(0,0,0,.08)"></div>
<div class="photo" style="left:120px;top:606px;width:148px;height:192px;background:linear-gradient(150deg,#3b93d8,#1c6db7 55%,#e9a6bf);border-radius:4px" role="img" aria-label="Photo of a gloved hand holding a bucket of spray bottles and cloths"></div>
<div class="abs" style="left:479px;top:787px;width:146px;height:185px;background:#fff;box-shadow:0 4px 14px rgba(0,0,0,.08)"></div>
<div class="photo" style="left:487px;top:795px;width:130px;height:169px;background:linear-gradient(160deg,#e9f1f3,#a9cfd9 60%,#5cb7c4);border-radius:4px" role="img" aria-label="Photo of a mop bucket on a tiled bathroom floor"></div>

<h2 class="section-title abs" style="left:630px;top:602px">We Are Very Experienced<br>In Cleaning Services</h2>
<p class="muted abs" style="left:630px;top:680px;width:360px">Vitae natoque tincidunt nunc sed dui nibh enim aliquam Lorem ipsum dolor sit amet consectetur.</p>

<div class="feature" style="top:736px">
  <div class="tick"><svg width="10" height="10" viewBox="0 0 10 10" fill="none" stroke="var(--teal)" stroke-width="1.6"><path d="M1.5 5l2.3 2.3L8.5 2.5"/></svg></div>
  <h4>We are Committed</h4>
  <p class="muted">Lorem ipsum dolor sit amet, consectetur dipiscing elit eiusmod tempor incididunt</p>
</div>
<div class="feature" style="top:818px">
  <div class="tick"><svg width="10" height="10" viewBox="0 0 10 10" fill="none" stroke="var(--teal)" stroke-width="1.6"><path d="M1.5 5l2.3 2.3L8.5 2.5"/></svg></div>
  <h4>Trusted Professionals</h4>
  <p class="muted">Lorem ipsum dolor sit amet, consectetur dipiscing elit eiusmod tempor incididunt</p>
</div>
<div class="feature" style="top:900px">
  <div class="tick"><svg width="10" height="10" viewBox="0 0 10 10" fill="none" stroke="var(--teal)" stroke-width="1.6"><path d="M1.5 5l2.3 2.3L8.5 2.5"/></svg></div>
  <h4>Highly Rated Cleaning</h4>
  <p class="muted">Lorem ipsum dolor sit amet, consectetur dipiscing elit eiusmod tempor incididunt</p>
</div>

<!-- SERVICES -->
<h2 class="section-title abs" style="left:0;width:1200px;text-align:center;top:1104px">Our Popular Services</h2>
<p class="muted abs" style="left:360px;width:480px;text-align:center;top:1151px">Vitae natoque tincidunt nunc sed dui nibh enim aliquam Lorem ipsum dolor sit amet consectetur. dictum iaculis eget more amet tincidunt urna massa done.</p>

<div class="arrow-btn" style="left:151px;top:1216px"><svg viewBox="0 0 12 12" fill="none" stroke="#555" stroke-width="1.5"><path d="M8 2L4 6l4 4"/></svg></div>
<div class="arrow-btn" style="left:1020px;top:1216px"><svg viewBox="0 0 12 12" fill="none" stroke="var(--blue)" stroke-width="1.5"><path d="M4 2l4 4-4 4"/></svg></div>

<div class="tab active" style="left:198px"></div>
<div class="tab" style="left:474px"></div>
<div class="tab" style="left:750px"></div>
<div class="tab-label active" style="left:198px"><svg width="18" height="16" viewBox="0 0 18 16" fill="none" stroke="#fff" stroke-width="1.3"><path d="M2 8L9 2l7 6M4 7v8h10V7"/></svg>Residential Cleaning</div>
<div class="tab-label" style="left:474px"><svg width="18" height="16" viewBox="0 0 18 16" fill="none" stroke="#777" stroke-width="1.3"><rect x="3" y="2" width="12" height="13"/><path d="M6 5h2M10 5h2M6 9h2M10 9h2"/></svg>Commercial Cleaning</div>
<div class="tab-label" style="left:750px"><svg width="18" height="16" viewBox="0 0 18 16" fill="none" stroke="#777" stroke-width="1.3"><path d="M2 15h14M4 15V6l5-4 5 4v9M7 15v-5h4v5"/></svg>New Construction Cleaning</div>

<div class="service-card">
  <div class="photo" style="left:0;top:0;width:449px;height:375px;background:linear-gradient(150deg,#f1efec,#d9d6d0 50%,#9fb06a 78%,#2f7d49)" role="img" aria-label="Photo of two cleaners in green overalls vacuuming and mopping a living room"></div>
  <svg class="abs" style="left:481px;top:28px" width="44" height="46" viewBox="0 0 44 46" fill="none" stroke="var(--blue)" stroke-width="1.6"><rect x="4" y="18" width="18" height="24" rx="2"/><path d="M8 18V10h10v8M10 10V4h6M26 30h14v12H26zM30 30v-6h6v6"/></svg>
  <h3 class="abs sans" style="left:481px;top:88px;color:var(--blue);font-weight:500;font-size:20px">Residential Cleaning</h3>
  <p class="abs" style="left:481px;top:124px;width:300px;font-size:11px;line-height:18px">Lorem ipsum dolor sit amet consectetur suspendisse nulla aliquam. Risus rutrum tellus ultrices amet facilisis.</p>
  <p class="muted abs" style="left:481px;top:185px;width:310px;font-size:10px">Commodo dictum iaculis eget mas phasellus ultrices nunc dignissim. Id nulla amet tincidunt urna sed massa the sed massa ultrices amet a egetristique maecenas condimentum dolor. dictum iaculis eget more amet tincidunt urna massa done.</p>
  <div class="abs" style="left:481px;top:324px;font-size:11px;color:#666">← PREV</div>
  <div class="abs" style="left:723px;top:324px;font-size:11px;color:var(--blue)">NEXT →</div>
</div>

<!-- TEAM -->
<h2 class="section-title abs" style="left:193px;top:1772px">Meet Our Professional<br>Team Members</h2>
<p class="muted abs" style="left:193px;top:1850px">Lorem ipsum dolor sit amet, consectetur dipiscing elit eiu incididunt.</p>
<div class="arrow-btn" style="left:939px;top:1839px"><svg viewBox="0 0 12 12" fill="none" stroke="#555" stroke-width="1.5"><path d="M8 2L4 6l4 4"/></svg></div>
<div class="arrow-btn" style="left:976px;top:1839px"><svg viewBox="0 0 12 12" fill="none" stroke="var(--blue)" stroke-width="1.5"><path d="M4 2l4 4-4 4"/></svg></div>

<!-- big blue + light background behind team/testimonials -->
<svg class="abs" style="left:0;top:1960px" width="1200" height="890" viewBox="0 0 1200 890" aria-hidden="true">
  <path d="M520 220 C700 200 900 180 1040 150 C1120 135 1170 120 1200 110 V878 H520 Z" fill="var(--teal-light)"/>
  <path d="M0 30 C80 20 130 160 240 230 C340 290 460 280 520 330 C560 370 540 460 520 560 C500 700 400 810 260 835 C160 852 60 840 0 830 Z" fill="var(--blue)"/>
</svg>

<div class="member" style="left:193px"><div class="photo" style="inset:0;background:linear-gradient(170deg,#5a5a5a,#2d2d2d 60%,#d4b43a)" role="img" aria-label="Photo of a smiling male cleaner holding a basket of supplies"></div><div class="shade"></div><div class="name">Evan Marsh</div><div class="role">Residential Cleaning</div></div>
<div class="member" style="left:402px"><div class="photo" style="inset:0;background:linear-gradient(170deg,#d9d9dd,#8f86a6 55%,#3e3a58)" role="img" aria-label="Photo of a female cleaner holding a sponge and spray bottle"></div><div class="shade"></div><div class="name">Lena Brooks</div><div class="role">Residential Cleaning</div></div>
<div class="member" style="left:610px"><div class="photo" style="inset:0;background:linear-gradient(170deg,#e0dfe3,#9a8d86 55%,#c44a3c)" role="img" aria-label="Photo of a male cleaner with apron holding a red bucket"></div><div class="shade"></div><div class="name">Marco Hale</div><div class="role">Residential Cleaning</div></div>
<div class="member" style="left:817px"><div class="photo" style="inset:0;background:linear-gradient(170deg,#f0f0f0,#cfcfd6 50%,#6a5aa0)" role="img" aria-label="Photo of a female cleaner beside a basket of cleaning products"></div><div class="shade"></div><div class="name">Tara Quinn</div><div class="role">Residential Cleaning</div></div>

<!-- TESTIMONIALS -->
<div class="photo" style="left:99px;top:2231px;width:367px;height:565px;background:linear-gradient(180deg,rgba(230,200,170,.55),rgba(200,190,170,.55) 45%,rgba(240,205,60,.7))" role="img" aria-label="Photo of a smiling male cleaner in apron standing with a yellow vacuum cleaner"></div>

<h2 class="section-title abs" style="left:513px;top:2300px">What Our Clients Say<br>About Us</h2>
<p class="muted abs" style="left:513px;top:2378px;width:370px">Vitae natoque tincidunt nunc sed dui nibh enim aliquam Lorem ipsum dolor sit amet consectetur.</p>

<div class="review" style="left:513px">
  <div class="avatar" style="background:linear-gradient(#9e8a7e,#4a5360)" role="img" aria-label="Client portrait"></div>
  <h4 class="sans">Lena Brooks</h4><div class="role">Residential Cleaning</div>
  <div class="stars"><svg width="118" height="14" viewBox="0 0 118 14" fill="var(--star)"><g id="s"><path d="M7 0l2 4.8 5 .4-3.8 3.3 1.2 5L7 10.8 2.6 13.5l1.2-5L0 5.2l5-.4z"/></g><use href="#s" x="26"/><use href="#s" x="52"/><use href="#s" x="78"/><use href="#s" x="104"/></svg></div>
  <p>"Commodo dictum iaculis eget mas phasellus ultrices nunc dignissim. massa the sed massa ultrices amet a egetristique maecenas condimentum dolor. dictum iaculis eget more amet tincidunt urna massa done."</p>
</div>
<div class="review" style="left:768px">
  <div class="avatar" style="background:linear-gradient(#c8a892,#36404e)" role="img" aria-label="Client portrait"></div>
  <h4 class="sans">Evan Marsh</h4><div class="role">Residential Cleaning</div>
  <div class="stars"><svg width="118" height="14" viewBox="0 0 118 14" fill="var(--star)"><use href="#s"/><use href="#s" x="26"/><use href="#s" x="52"/><use href="#s" x="78"/><use href="#s" x="104"/></svg></div>
  <p>"Commodo dictum iaculis eget mas phasellus ultrices nunc dignissim. massa the sed massa ultrices amet a egetristique maecenas condimentum dolor. dictum iaculis eget more amet tincidunt urna massa done."</p>
</div>
<div class="review" style="left:1025px;opacity:.45">
  <div class="avatar" style="background:linear-gradient(#e3cf9e,#b6a27a)" role="img" aria-label="Client portrait"></div>
  <h4 class="sans">Ravi Dalton</h4><div class="role">Residential Cleaning</div>
  <div class="stars"><svg width="118" height="14" viewBox="0 0 118 14" fill="var(--star)"><use href="#s"/><use href="#s" x="26"/><use href="#s" x="52"/><use href="#s" x="78"/><use href="#s" x="104"/></svg></div>
  <p>"Commodo dictum iaculis eget mas phasellus ultrices nunc dignissim. massa the sed massa ultrices amet a egetristique maecenas condimentum dolor. dictum iaculis eget more amet tincidunt urna massa done."</p>
</div>
<div class="arrow-btn" style="left:514px;top:2751px"><svg viewBox="0 0 12 12" fill="none" stroke="#555" stroke-width="1.5"><path d="M8 2L4 6l4 4"/></svg></div>
<div class="arrow-btn" style="left:551px;top:2751px"><svg viewBox="0 0 12 12" fill="none" stroke="var(--blue)" stroke-width="1.5"><path d="M4 2l4 4-4 4"/></svg></div>

<!-- CONTACT -->
<svg class="abs" style="left:560px;top:2870px" width="560" height="500" viewBox="0 0 560 500" aria-hidden="true">
  <path d="M40 80 C120 10 260 0 330 40 C380 70 360 140 430 190 C520 250 540 340 500 420 C470 480 400 490 330 470 C240 445 150 470 90 430 C20 380 -10 150 40 80 Z" fill="var(--teal-light)"/>
</svg>
<h2 class="section-title abs" style="left:193px;top:2998px;font-weight:400">Les’t talk<br><span style="font-weight:500">on something great together</span></h2>

<div class="contact-row" style="top:3094px"><svg width="22" height="16" viewBox="0 0 24 18" fill="none" stroke="var(--blue)" stroke-width="2"><rect x="1" y="1" width="22" height="16" rx="2"/><path d="M1 2l11 8 11-8"/></svg>hello@brightnestclean.com</div>
<div class="contact-row" style="top:3142px"><svg width="22" height="20" viewBox="0 0 24 24" fill="var(--blue)"><path d="M6.6 10.8a15.1 15.1 0 0 0 6.6 6.6l2.2-2.2c.3-.3.7-.4 1-.2 1.1.4 2.3.6 3.6.6.6 0 1 .4 1 1V20c0 .6-.4 1-1 1A17 17 0 0 1 3 4c0-.6.4-1 1-1h3.5c.6 0 1 .4 1 1 0 1.3.2 2.5.6 3.6.1.3 0 .7-.2 1z"/></svg>(555) 014-3820</div>
<div class="contact-row" style="top:3193px"><svg width="22" height="24" viewBox="0 0 24 24" fill="var(--blue)"><path d="M12 1a8 8 0 0 0-8 8c0 6 8 14 8 14s8-8 8-14a8 8 0 0 0-8-8zm0 11a3 3 0 1 1 0-6 3 3 0 0 1 0 6z"/></svg>45 Harbor Lane</div>

<div class="abs" style="left:611px;top:2906px;width:394px;height:419px;background:#fff;box-shadow:0 4px 18px rgba(0,0,0,.06)"></div>
<h3 class="abs sans" style="left:633px;top:2940px;font-weight:500;font-size:19px">Contact us</h3>
<p class="muted abs" style="left:633px;top:2974px;width:320px">Lorem ipsum dolor sit amet consectetur Vitae natoque tincidunt nunc sed dui nibh enim aliquam.</p>
<div class="field" style="top:3027px">Name</div>
<div class="field" style="top:3073px">Email</div>
<div class="field" style="top:3119px;height:81px">Message</div>
<div class="abs" style="left:633px;top:3220px;display:flex;align-items:center;gap:6px;font-size:7px;color:#666"><span style="width:9px;height:9px;border:1px solid #999;display:inline-block"></span>I would like to receive the newsletter</div>
<div class="btn" style="left:633px;top:3256px;width:125px;height:35px">Discover Services</div>

<!-- FOOTER -->
<footer class="footer">
  <svg class="abs" style="left:700px;top:0" width="500" height="250" viewBox="0 0 500 250" aria-hidden="true">
    <path d="M60 0 C120 60 200 40 260 90 C320 140 360 200 500 180 V0 Z" fill="#fff" opacity=".08"/>
  </svg>
  <div class="abs" style="left:193px;top:48px;display:flex;align-items:center;gap:8px"><div style="width:16px;height:16px;background:#fff;border-radius:3px"></div><div class="sans" style="font-weight:600;font-size:16px;letter-spacing:.5px">BRIGHTNEST</div></div>
  <p class="abs" style="left:193px;top:92px;width:225px;font-size:9px;line-height:16px;opacity:.9">Lorem ipsum dolor sit amet consectetur suspendisse nulla aliquam. Risus rutrum tellus ultrices amet facilisis. Vitae natoque tincidunt nunc sed dui nibh enim aliquam Lorem ipsum dolor sit amet consectetur.</p>
  <div class="abs" style="left:193px;top:222px;display:flex;gap:14px">
    <span style="width:10px;height:10px;border-radius:50%;background:#fff"></span>
    <span style="width:10px;height:10px;border-radius:50%;background:#fff"></span>
    <span style="width:10px;height:10px;border-radius:50%;background:#fff"></span>
    <span style="width:10px;height:10px;border-radius:50%;background:#fff"></span>
  </div>
  <div class="abs" style="left:502px;top:64px"><h4 class="sans">Quick Links</h4><ul><li>Home</li><li>About</li><li>Our Services</li><li>Contact Us</li></ul></div>
  <div class="abs" style="left:658px;top:64px"><h4 class="sans">Our Services</h4><ul><li>Residential Cleaning</li><li>Commercial Cleaning</li><li>New Construction Cleaning</li><li>Apartment Turn cleaning</li></ul></div>
  <div class="abs" style="left:871px;top:64px"><h4 class="sans">Contact Us</h4><ul><li>hello@brightnestclean.com</li><li style="opacity:.6">For Service inquiry</li><li style="font-size:11px">(555) 014-3820</li></ul></div>
  <div class="abs" style="left:719px;top:222px;font-size:9px;opacity:.9">Copyright © 2024 BrightNest Cleaning. All rights reserved.</div>
</footer>

</body>
</html>
```